Business Card Design for boarding house accomodation business

I need a business card design for my Sydney based boarding house business accomodation. providing rooms for rent in Sydney Australia with shard bathroom and kitchen.
The front of card, are my details with details of head office and the rear of card to have details of locations providing rooms for rent.

Industry/Entity Type

Business

Contact Information for Business Card

Front of card details:
HOLLOWAY MANAGEMENT PTY LTD t/a
LINDFIELD'S GUEST HOUSE
ABN:52907318460
Daniel Kavanagh
48 Clement st
Newtown 2042
Mobile:0417386920
Email:daniel@lindfieldsguesthouse.example.au

Back of Card:
Locations:
-48 Clement st
Newtown 2042

-362 Harlow st
Erskineville 2043

-87 Fenwick st
Bondi 2026

-294 Ashcombe rd
Marrickville 2043

```html
<!DOCTYPE html>
<html lang="en">
<head>
<meta charset="utf-8">
<title>Lindfield's Guest House – Business Card</title>
<link rel="stylesheet" href="https://fonts.googleapis.com/css2?family=Bodoni+Moda:wght@500;600&family=Noto+Sans:wght@400&display=swap">
<style>
  :root {
    --page-bg: #ecebea;
    --satin-light: #f4f4f4;
    --satin-mid: #d9d9d9;
    --satin-dark: #bdbdbd;
    --ink: #111111;
    --back-bg: #000000;
    --back-ink: #ffffff;
  }
  * { margin: 0; padding: 0; box-sizing: border-box; }
  html, body { width: 1189px; height: 1200px; overflow: hidden; }
  body { background: var(--page-bg); position: relative; font-family: "Noto Sans", sans-serif; }

  .card { position: absolute; left: 140px; width: 917px; height: 524px; overflow: hidden; }
  .card--front { top: 45px; }
  .card--back { top: 624px; background: var(--back-bg); color: var(--back-ink); }

  .satin {
    position: absolute; inset: 0;
    background:
      radial-gradient(ellipse 60% 40% at 30% 30%, var(--satin-light), transparent 70%),
      radial-gradient(ellipse 50% 35% at 75% 70%, var(--satin-light), transparent 70%),
      linear-gradient(135deg, var(--satin-mid) 0%, var(--satin-light) 35%, var(--satin-dark) 55%, var(--satin-light) 75%, var(--satin-mid) 100%);
  }

  .centered { position: absolute; left: 0; right: 0; text-align: center; color: var(--ink); transform: translateY(-50%); white-space: nowrap; }
  .company, .trading-name { font-family: "Bodoni Moda", serif; font-weight: 600; font-size: 50px; line-height: 1; }
  .company { top: 100px; }
  .trading-name { top: 155px; }
  .person { top: 259px; font-family: "Bodoni Moda", serif; font-weight: 600; font-size: 34px; }
  .abn { top: 302px; font-size: 23px; }
  .contact { font-size: 24px; }
  .contact--phone { top: 389px; }
  .contact--address { top: 425px; }
  .contact--email { top: 461px; }

  .rule { position: absolute; height: 2px; background: var(--ink); }
  .rule--upper { top: 220px; left: 56px; width: 801px; }
  .rule--lower { top: 332px; left: 84px; width: 745px; }

  .locations-title { position: absolute; left: 76px; top: 90px; transform: translateY(-50%); font-family: "Bodoni Moda", serif; font-weight: 600; font-size: 46px; }
  .locations-rule { position: absolute; left: 310px; right: 0; top: 95px; height: 2px; background: var(--back-ink); }

  .location-list { list-style: none; }
  .location { position: absolute; left: 204px; display: flex; align-items: center; gap: 18px; font-size: 24px; transform: translateY(-50%); white-space: nowrap; }
  .location svg { width: 17px; height: 24px; fill: var(--back-ink); }
  .location:nth-child(1) { top: 222px; }
  .location:nth-child(2) { top: 279px; }
  .location:nth-child(3) { top: 342px; }
  .location:nth-child(4) { top: 400px; }
</style>
</head>
<body>
  <section class="card card--front">
    <div class="satin" role="img" aria-label="Soft white satin fabric background"></div>
    <h1 class="centered company">Holloway Management Pty ltd</h1>
    <h2 class="centered trading-name">Lindfield’S Guest House</h2>
    <div class="rule rule--upper"></div>
    <p class="centered person">Daniel Kavanagh</p>
    <p class="centered abn">ABN:52907318460</p>
    <div class="rule rule--lower"></div>
    <p class="centered contact contact--phone">0417386920</p>
    <p class="centered contact contact--address">48 Clement st Newtown 2042</p>
    <p class="centered contact contact--email">daniel@lindfieldsguesthouse.example.au</p>
  </section>

  <section class="card card--back">
    <h2 class="locations-title">Locations</h2>
    <div class="locations-rule"></div>
    <ul class="location-list">
      <li class="location"><svg viewBox="0 0 17 24"><path d="M8.5 0C3.8 0 0 3.7 0 8.3 0 14.5 8.5 24 8.5 24S17 14.5 17 8.3C17 3.7 13.2 0 8.5 0zm0 11.5a3.3 3.3 0 1 1 0-6.6 3.3 3.3 0 0 1 0 6.6z"/></svg>87 Fenwick st Bondi 2026</li>
      <li class="location"><svg viewBox="0 0 17 24"><path d="M8.5 0C3.8 0 0 3.7 0 8.3 0 14.5 8.5 24 8.5 24S17 14.5 17 8.3C17 3.7 13.2 0 8.5 0zm0 11.5a3.3 3.3 0 1 1 0-6.6 3.3 3.3 0 0 1 0 6.6z"/></svg>48 Clement st Newtown 2042</li>
      <li class="location"><svg viewBox="0 0 17 24"><path d="M8.5 0C3.8 0 0 3.7 0 8.3 0 14.5 8.5 24 8.5 24S17 14.5 17 8.3C17 3.7 13.2 0 8.5 0zm0 11.5a3.3 3.3 0 1 1 0-6.6 3.3 3.3 0 0 1 0 6.6z"/></svg>362 Harlow st Erskineville 2043</li>
      <li class="location"><svg viewBox="0 0 17 24"><path d="M8.5 0C3.8 0 0 3.7 0 8.3 0 14.5 8.5 24 8.5 24S17 14.5 17 8.3C17 3.7 13.2 0 8.5 0zm0 11.5a3.3 3.3 0 1 1 0-6.6 3.3 3.3 0 0 1 0 6.6z"/></svg>294 Ashcombe rd Marrickville 2043</li>
    </ul>
  </section>
</body>
</html>
```